need web page design for BrightOakly.com

This site sells information products for international corporate users. It is selling Silver Pathways and Quarterly Ledger Craft, a product on international business tax, and other books. See sample. I will also upload a possible logo. Upload 2 The tag line is Predicting and Solving Business and Law Issues for the Multinational Upload 3 is a sample theme from Shopify, the site I will use. The sample is for ideas only. I am not wedded to it. Upload 4 is Meridian Ledger Journal Pge

Number of Pages Required

2 page

```html
<!DOCTYPE html>
<html lang="en">
<head>
<meta charset="utf-8">
<title>BrightOakly.com</title>
<link href="https://fonts.googleapis.com/css2?family=Arimo:ital,wght@0,400;0,700;1,400&display=swap" rel="stylesheet">
<style>
:root{
  --brand:#237ca3;
  --nav:#06161d;
  --page:#f7f7f7;
  --panel:#f5f5f5;
  --ink:#111;
  --white:#fff;
  --accent-red:#e02020;
  --gold:#f2c400;
  --rule:#c8a800;
  --grey:#9a9a9a;
  --black:#000;
}
*{box-sizing:border-box;margin:0;padding:0}
html,body{width:1058px;height:1200px;overflow:hidden}
body{position:relative;background:var(--page);font-family:'Arimo',Arial,sans-serif;color:var(--ink)}
.abs{position:absolute}
.top-band{left:0;top:0;width:1058px;height:289px;background:var(--brand)}
.brand-name{left:153px;top:26px;font-size:36px;font-weight:700;letter-spacing:5px;color:var(--ink);line-height:44px}
.tagline{left:148px;top:73px;font-size:10px;font-weight:700;color:var(--white);letter-spacing:.6px}
.cart{left:908px;top:4px;width:25px;height:25px;border-radius:50%;background:#0f4f6e}
.account{top:33px;font-size:10px;font-weight:700;color:var(--white);letter-spacing:.5px}
.search{left:750px;top:56px;width:188px;height:32px;border-radius:5px;background:var(--page);font-size:12.5px;color:#333;text-align:right;padding:9px 10px 0 0;letter-spacing:.5px}
.nav{left:120px;top:102px;width:827px;height:68px;background:var(--nav);border-top:1px solid var(--rule)}
.nav-home{left:152px;top:122px;width:97px;height:32px;border-radius:4px;background:var(--panel);color:#5a4a1a;font-size:13.5px;text-align:center;line-height:32px}
.nav-item{top:129px;font-size:13.5px;color:var(--white);letter-spacing:.3px}
.hero{left:120px;top:170px;width:827px;height:301px;background:var(--panel)}
.hero-shadow{left:140px;top:468px;width:787px;height:12px;background:radial-gradient(ellipse at 50% 0,rgba(0,0,0,0) 60%,rgba(0,0,0,0));}
.hero-shadow::before,.hero-shadow::after{content:"";position:absolute;top:0;width:260px;height:10px;background:linear-gradient(to bottom,rgba(0,0,0,.18),rgba(0,0,0,0))}
.hero-shadow::before{left:0;border-radius:0 0 0 100%}
.hero-shadow::after{right:0;border-radius:0 0 100% 0}
.hero-title{left:182px;top:254px;font-size:31px;color:var(--brand);letter-spacing:2.5px}
.hero-text{left:187px;top:304px;width:660px;font-size:12px;line-height:17px;letter-spacing:1px;color:#222}
.read-more{left:187px;top:352px;width:128px;height:31px;border:1px solid var(--accent-red);border-radius:5px;color:var(--accent-red);font-style:italic;font-size:13px;text-align:center;line-height:29px;letter-spacing:.5px}
.slider-dots{left:505px;top:426px}
.welcome-title{left:150px;top:529px;font-size:22px;letter-spacing:.8px}
.welcome-rule{left:150px;top:562px;width:510px;height:1px;background:var(--ink)}
.welcome-text{left:150px;top:571px;width:770px;font-size:12.5px;line-height:18px;letter-spacing:1px;color:#222}
.news-title{left:150px;top:711px;font-size:19px;letter-spacing:.5px}
.news-card{top:748px;width:394px;height:161px;background:var(--black)}
.news-image{position:absolute;left:21px;top:23px;width:120px;height:120px;border-radius:50%;background:var(--page);font-size:17px;letter-spacing:1.5px;text-align:center;line-height:120px;color:#222}
.news-head{position:absolute;left:160px;top:28px;font-size:17px;color:var(--white);letter-spacing:.6px}
.news-rule{position:absolute;left:160px;top:57px;width:216px;height:1px;background:var(--white)}
.news-text{position:absolute;left:161px;top:63px;width:215px;font-size:11.5px;line-height:17px;color:var(--white);letter-spacing:.8px}
.news-more{position:absolute;left:161px;top:120px;font-size:9.5px;font-style:italic;color:var(--gold);text-decoration:underline}
.arrow-btn{top:880px;width:30px;height:30px;background:#151515;border-radius:3px}
.section-title{top:934px;font-size:19.5px}
.section-rule{top:971px;width:393px;height:1px;background:var(--ink)}
.quick-link{left:160px;font-size:13px;color:var(--accent-red);letter-spacing:.8px}
.social{top:987px;display:flex;align-items:center;gap:6px;font-size:12px;color:#666}
.social i{display:block;width:32px;height:32px;border-radius:50%;background:var(--grey)}
.footer{left:0;top:1085px;width:1058px;height:115px;background:var(--black)}
.pay{top:1122px;width:67px;height:41px;background:var(--white);font-size:10px;font-weight:700;color:#1a2a5a;text-align:center;line-height:41px;letter-spacing:.3px}
.copyright{left:0;width:1058px;top:1180px;text-align:center;font-size:11px;font-weight:700;color:var(--white);letter-spacing:1px}
</style>
</head>
<body>
<div class="abs top-band"></div>
<div class="abs brand-name">BrightOakly.com</div>
<div class="abs tagline">Predicting and Providing Business and Law Solutions For Multinational Corporations</div>
<div class="abs cart">
  <svg width="25" height="25" viewBox="0 0 25 25" aria-hidden="true"><path d="M7 8h2l2 7h6l1.5-5H10" fill="none" stroke="#fff" stroke-width="1"/><circle cx="12" cy="17.5" r="1" fill="#fff"/><circle cx="16" cy="17.5" r="1" fill="#fff"/></svg>
</div>
<div class="abs account" style="left:852px">LogIn</div>
<div class="abs account" style="left:892px">Register</div>
<div class="abs search">Search</div>

<nav class="abs nav"></nav>
<div class="abs nav-home">Home</div>
<div class="abs nav-item" style="left:284px">Our Products</div>
<div class="abs nav-item" style="left:407px">Latest News</div>
<div class="abs nav-item" style="left:528px">Contact</div>
<div class="abs nav-item" style="left:619px">Business Guides</div>
<div class="abs nav-item" style="left:768px">About Us</div>

<section class="abs hero"></section>
<div class="abs hero-shadow"></div>
<h1 class="abs hero-title" style="font-weight:400">BrightOakly.com</h1>
<p class="abs hero-text">This lorem ipsum generator is made for all the webdesigners, designers, webmasters and others who need lorem ipsum. Generator is made the way that everyone can use it, but</p>
<div class="abs read-more">read more.</div>
<svg class="abs slider-dots" width="36" height="12" viewBox="0 0 36 12" aria-hidden="true"><path d="M1 6l5-3v6z" fill="#0c2a44"/><circle cx="19" cy="6" r="3.5" fill="#1d5fb0"/><circle cx="31" cy="6" r="3.5" fill="#1d5fb0"/></svg>

<h2 class="abs welcome-title" style="font-weight:400">Welcome To Lorem Ipsum Generator</h2>
<div class="abs welcome-rule"></div>
<p class="abs welcome-text">This lorem ipsum generator is made for all the webdesigners, designers, webmasters and others who need lorem ipsum. Generator is made the way that everyone can use it, but especially for projects which need html markup. You can decide which html tags you want and our generator will generate just as you specified.<br>Pretty cool, isn't it?</p>

<h2 class="abs news-title" style="font-weight:400">NEWS</h2>
<article class="abs news-card" style="left:150px">
  <div class="news-image" role="img" aria-label="News story image">IMAGE</div>
  <div class="news-head">Lorem Ipsum Generator</div>
  <div class="news-rule"></div>
  <p class="news-text">This lorem ipsum generator is made for all the webdesigners, designers, webmasters and</p>
  <div class="news-more">Read more..</div>
</article>
<article class="abs news-card" style="left:552px">
  <div class="news-image" role="img" aria-label="News story image">IMAGE</div>
  <div class="news-head">Lorem Ipsum Generator</div>
  <div class="news-rule"></div>
  <p class="news-text">This lorem ipsum generator is made for all the webdesigners, designers, webmasters and</p>
  <div class="news-more">Read more..</div>
</article>
<div class="abs arrow-btn" style="left:512px"><svg width="30" height="30" viewBox="0 0 30 30" aria-hidden="true"><path d="M17 10l-4 5 4 5" fill="none" stroke="#fff" stroke-width="2"/></svg></div>
<div class="abs arrow-btn" style="left:552px"><svg width="30" height="30" viewBox="0 0 30 30" aria-hidden="true"><path d="M13 10l4 5-4 5" fill="none" stroke="#fff" stroke-width="2"/></svg></div>

<h3 class="abs section-title" style="left:151px;font-weight:400">Quick Links</h3>
<div class="abs section-rule" style="left:150px"></div>
<div class="abs quick-link" style="top:993px;text-decoration:underline">Search</div>
<div class="abs quick-link" style="top:1018px">About Us</div>

<h3 class="abs section-title" style="left:565px;font-weight:400">Follow Us</h3>
<div class="abs section-rule" style="left:552px"></div>
<div class="abs social" style="left:566px"><i></i>Chirpline</div>
<div class="abs social" style="left:660px"><i></i>Friendsy</div>

<footer class="abs footer"></footer>
<div class="abs pay" style="left:394px">CoinPass</div>
<div class="abs pay" style="left:472px">Vantra</div>
<div class="abs pay" style="left:551px">Amberline</div>
<div class="abs pay" style="left:625px">Northway</div>
<div class="abs copyright">Copyright © 2014 BrightOakly.com | Powered by Abc</div>
</body>
</html>
```